Wine label - premium, elegant & classic

We are a young husband and wife team who have worked in the wine industry for 10+ years. This year we've finally had the opportunity to make our own wine and release our own brand. Our wines are boutique and sell at a mid-premium price (we don't make a lot) so we're looking for a label design that can reflect this premium nature and mixes traditional design elements with modern reflections.

The brand is called: L&T

Reason: We've received some great design concepts over the past week which we would happily pay for, so we've decided to guarantee payment and extend the deadline to allow time for more designs to be sent through. A BIG thanks to all who have already submitted, your designs are still under consideration. Cheers, T.

A big thank you to all for taking the time to submit your beautiful designs to our project.  We now have the very tough job of looking over each of them and selecting only one.  We hope to come to a decision in the next day or two, so hopefully we won't keep you waiting too long!

Cheers, and thanks again

L&T.                                   

Target Market(s)

30 - 45 year old female and male wine drinkers

Requirements
Must have
• Can we please see two versions of the one design - one for a red wine and one for a white wine.

The front labels needs to include the following information:
1. Brand name: L&T
2. Wine varieties: Pinot Noir (red wine) and Sauvignon Blanc (white wine)
3. Vintage: 2012 for both
4. Region: Yarra Valley
5. GI: Wine of Australia (not essential to be on front label)

The back label needs to include the following:
1. The brand name: L&T
2. Variety, vintage, region and volume (the volume must be 4mm in height)
3. Room for product description - approx. 30-40 words.
4. Alcohol statement (no size restriction, pls use 12.5% ALC/VOL as example)
5. Standard drinks (no size restriction, pls use 'Approx.7.8 standard drinks' as example)
6. Sulphites statement: "Sulphites added."
7. Allergen statement: "Fined with the aid of egg and milk products and traces may remain."
8. Room for address: Approx. 20 words
9. "Wine of Australia" - no size restriction, just needs to be legible

Packaging presentation:
Pinot Noir is a red wine and Sauvignon Blanc is a white wine.
Labels for both need to be shown on premium punted burgundy bottles (pls see example: http://www.velmorapack.com/products_services/kfq_premium_burgundy_750_ml_wine_bottle.html)
Nice to have
• We would like the design to embody the following elements:
1. Classically modern
2. Clean and simple
3. Elegance
4. Restricted use of colours (ideally just black/grey, white/buff and perhaps one other)

Some design examples of what we like:
1. http://www.fernandgulls.com.au/sangiovese-tasting-notes/
2. http://quollridge.com/Wines/Quoll-Ridge-Vineyard/Range/2010-Quoll-Ridge-Single-Vineyard-Pinot-Noir-.htm
Should not have
• Preferrably won't have any photos or drawings unless you feel there is a simple symbol or image that could be used to enhance the design.

Restricted use of colours - more muted, conservative tones.

```html
<!DOCTYPE html>
<html lang="en">
<head>
<meta charset="utf-8">
<title>L&amp;T Pinot Noir 2012 – Front Label</title>
<link rel="stylesheet" href="https://fonts.googleapis.com/css2?family=Libre+Franklin:wght@400&family=Cormorant+Garamond:ital,wght@0,400;1,400&display=swap">
<style>
  :root {
    --backdrop: #161513;
    --label-deep: #0a1716;
    --label-teal: #143331;
    --ink-cream: #e8e5de;
    --ink-soft: #c9c6bf;
    --ink-muted: #8f948f;
  }
  html, body {
    margin: 0;
    padding: 0;
    width: 1200px;
    height: 1200px;
    overflow: hidden;
    background: var(--backdrop);
  }
  .canvas {
    position: relative;
    width: 1200px;
    height: 1200px;
    background: var(--backdrop);
  }
  .front-label {
    position: absolute;
    left: 250px;
    top: 110px;
    width: 700px;
    height: 980px;
    background:
      radial-gradient(ellipse at 50% 35%, var(--label-teal) 0%, transparent 70%),
      linear-gradient(160deg, #122c2a 0%, var(--label-deep) 100%);
  }
  .brand-name {
    position: absolute;
    left: 40px;
    top: 120px;
    margin: 0;
    font-family: "Cormorant Garamond", Georgia, serif;
    font-weight: 400;
    font-size: 190px;
    line-height: 1;
    letter-spacing: 4px;
    color: var(--ink-cream);
  }
  .vintage-region {
    position: absolute;
    left: 44px;
    top: 390px;
    margin: 0;
    font-family: "Libre Franklin", Arial, sans-serif;
    font-weight: 400;
    font-size: 40px;
    line-height: 1;
    letter-spacing: 3px;
    color: var(--ink-cream);
  }
  .vintage-region .vintage { margin-right: 28px; }
  .variety {
    position: absolute;
    left: 0;
    width: 700px;
    top: 600px;
    margin: 0;
    text-align: center;
    font-family: "Cormorant Garamond", Georgia, serif;
    font-style: italic;
    font-size: 40px;
    color: var(--ink-muted);
  }
  .origin {
    position: absolute;
    left: 40px;
    width: 620px;
    top: 760px;
    margin: 0;
    text-align: left;
    font-family: "Cormorant Garamond", Georgia, serif;
    font-weight: 400;
    font-size: 50px;
    line-height: 1;
    letter-spacing: 2px;
    color: var(--ink-soft);
  }
</style>
</head>
<body>
  <main class="canvas">
    <section class="front-label" aria-label="L&amp;T Yarra Valley Pinot Noir front label">
      <h1 class="brand-name">L&amp;T</h1>
      <p class="vintage-region"><span class="vintage">2012</span><span class="region">YARRA VALLEY</span></p>
      <p class="variety">Pinot Noir</p>
      <p class="origin">WINE OF AUSTRALIA</p>
    </section>
  </main>
</body>
</html>
```